I am a Financial Adviser specialising in Aged Care Advice. We provide financial advice and assistance to families with loved ones entering an Aged Care facility.
We need a flyer detailing the Aged Care Packages that we offer. There will be 3 main packages & then other add ons. I need an area where the client can sign off on the package/s that they choose. I have attached a sample to demonstrate the required layout, and a copy of content. I would like the flyer to have an image as per the attached sample, and to be designed in soft pastels, blues, greens.

Financial

```html
<!DOCTYPE html>
<html lang="en">
<head>
<meta charset="utf-8">
<title>Silver Harbour – Aged Care Services Flyer</title>
<link href="https://fonts.googleapis.com/css2?family=Libre+Baskerville:wght@400;700&family=Great+Vibes&family=Didact+Gothic&family=Cormorant+Garamond:wght@700&family=Arimo:wght@400;700&display=swap" rel="stylesheet">
<style>
  :root{
    --page:#ffffff;
    --mint:#d3efec;
    --mint-soft:#e6f6f4;
    --teal:#3fbfa8;
    --teal-dark:#2a9f8d;
    --gold:#d6a72a;
    --ink:#1a1a1a;
    --grey:#555;
    --grass:#8fae4e;
    --leaf:#cfe0a0;
  }
  *{box-sizing:border-box;margin:0;padding:0}
  html,body{width:1200px;height:1000px;overflow:hidden;background:var(--page)}
  body{position:relative;font-family:"Didact Gothic",Arial,sans-serif;color:var(--ink)}

  .sheet{position:absolute;top:96px;width:578px;height:818px;overflow:hidden}
  .sheet--front{left:14px;background:linear-gradient(180deg,#fff 0,#fff 300px,var(--mint-soft) 420px,var(--mint) 818px)}
  .sheet--back{left:608px;background:linear-gradient(180deg,var(--mint-soft),var(--mint))}

  .hero-photo{position:absolute;left:0;top:0;width:578px;height:360px;
    background:
      radial-gradient(ellipse at 70% 20%,#f4f7e6 0,rgba(244,247,230,0) 45%),
      linear-gradient(180deg,#a9c47a 0%,#86a651 45%,#9fbc63 75%,rgba(211,239,236,0) 100%);}
  .brand{position:absolute;left:200px;top:212px;font-family:"Libre Baskerville",Georgia,serif;font-weight:700;font-size:22px;color:#1b1b1b;display:flex;align-items:center;gap:8px}
  .brand__dot{width:14px;height:14px;background:var(--gold)}
  .title{position:absolute;left:0;width:578px;top:280px;text-align:center;font-family:"Cormorant Garamond",Georgia,serif;font-weight:700;font-size:62px;color:var(--gold);letter-spacing:-.5px;text-shadow:0 0 6px #fff,0 0 12px #fff}

  .package{position:absolute;left:32px;width:516px;background:#fff;border:1.5px solid #333;border-radius:14px;box-shadow:3px 4px 6px rgba(0,0,0,.35);padding:10px 16px}
  .package--essentials{top:366px;height:132px}
  .package--advantage{top:516px;height:134px}
  .package--platinum{top:666px;height:132px}
  .package__tag{position:absolute;right:36px;top:-20px;font-family:"Great Vibes",cursive;font-size:30px;color:var(--teal);background:linear-gradient(180deg,transparent 50%,#fff 50%);padding:0 8px;line-height:1}
  .package__name{font-family:"Libre Baskerville",Georgia,serif;font-size:15px;display:flex;align-items:center;gap:8px}
  .package__name b{font-weight:700}
  .box{display:inline-block;width:13px;height:13px;border:1.6px solid #222;background:#fff;flex:none}
  .package__lead{font-family:"Libre Baskerville",Georgia,serif;font-size:10px;margin:2px 0 8px 34px}
  .package__plus{font-family:"Arimo",Arial,sans-serif;font-weight:700;font-size:14px;margin-top:-2px}
  .package__plus span{color:var(--gold)}
  .features{display:grid;grid-template-columns:236px 1fr;column-gap:10px;font-size:10.5px;line-height:1.3;list-style:none}
  .features li::before{content:"• "}
  .note{font-size:7.5px;margin-top:14px}

  .options-card{position:absolute;left:26px;top:32px;width:530px;height:756px;background:#fff;border:1.5px solid #333;border-radius:16px;box-shadow:3px 4px 6px rgba(0,0,0,.35)}
  .options-card h2{position:absolute;left:22px;top:18px;font-family:"Libre Baskerville",Georgia,serif;font-weight:700;font-size:19px;color:var(--teal)}
  .option{position:absolute;left:22px;width:484px;display:flex;gap:8px}
  .option h3{font-family:"Arimo",Arial,sans-serif;font-size:12px;font-weight:700;color:var(--teal)}
  .option p{font-size:9.5px;line-height:1.25}
  .option .box{margin-top:1px}

  .sign-off{position:absolute;left:14px;top:398px;width:496px;height:226px;border:1px solid #444;padding:18px 10px 0 10px;font-family:"Arimo",Arial,sans-serif;font-size:11px;line-height:1.6}
  .sign-row{position:absolute;display:flex;gap:16px}
  .sign{width:106px;border-top:1px solid #222;text-align:center;font-weight:700;font-size:11.5px;padding-top:4px}
  .dateline{position:absolute;font-size:11px;letter-spacing:28px}

  .legal{position:absolute;left:20px;top:642px;width:486px;font-family:"Arimo",Arial,sans-serif;font-size:7.6px;line-height:1.3}
  .legal h4{font-size:8px}
  .legal p+p{margin-top:5px}
</style>
</head>
<body>

<section class="sheet sheet--front">
  <div class="hero-photo" role="img" aria-label="Photograph of a smiling three-generation family sitting together on grass in a sunny park"></div>
  <div class="brand"><span class="brand__dot"></span>Silver Harbour</div>
  <h1 class="title">Aged Care Services</h1>

  <article class="package package--essentials">
    <span class="package__tag">Peace of Mind</span>
    <div class="package__name"><span class="box"></span><span><b>ESSENTIALS</b> Package $770 .......</span></div>
    <div class="package__lead">When you know what you want….</div>
    <ul class="features">
      <li>Explanation of Aged Care Fees and Charges.</li><li>Preliminary Aged Care Costs.*</li>
      <li>Preliminary Home/Assets Assessment.*</li><li>Estimated Cash Flow Scenario.*</li>
      <li>Estimated Means Tested Fee Calculation.*</li>
    </ul>
    <p class="note">*Please note this is general factual information only.  We do not provide any specific personal financial advice.</p>
  </article>

  <article class="package package--advantage">
    <span class="package__tag">Confidence</span>
    <div class="package__name"><span class="box"></span><span><b>ADVANTAGE</b> Package $2,970</span></div>
    <div class="package__lead">…..When you need to know all the options….</div>
    <div class="package__plus"><span>ESSENTIALS</span> Package plus</div>
    <ul class="features">
      <li>Analyse and Strategize Aged Care costs.</li><li>Maximise Age Pension Income (where possible).</li>
      <li>Compare up to 5 Strategy options.</li><li>Prepare a Full Statement of Advice (SOA).</li>
      <li>Minimise Aged Care Costs (where possible).</li><li>Implementation of Aged Care Strategy.</li>
    </ul>
  </article>

  <article class="package package--platinum">
    <span class="package__tag">Convenience</span>
    <div class="package__name"><span class="box"></span><span><b>PLATINUM</b> Package $5,940.......</span></div>
    <div class="package__lead">When you need someone to take charge….</div>
    <div class="package__plus"><span>ADVANTAGE</span> Package plus</div>
    <ul class="features">
      <li>Liase with the Aged Care Facility.</li><li style="visibility:hidden">.</li>
      <li>CentreLink/DVA Nominee.</li><li>Post Implementation SOA (if required).</li>
      <li>Post Entry Review.</li><li>Annual Review (one).</li>
    </ul>
  </article>
</section>

<section class="sheet sheet--back">
  <div class="options-card">
    <h2>EXTRA CHOICE OPTIONS</h2>

    <div class="option" style="top:56px"><span class="box"></span><div><h3>CentreLink/DVA Nominee $1,100</h3><p>Communicate with CentreLink/DVA on behalf of our client/s, and undertake all changes and updates to details, as directed by our client.</p></div></div>
    <div class="option" style="top:104px"><span class="box"></span><div><h3>Post Implementation Statement of Advice $1,650</h3><p>Revise our original Advice Statement for any changes of circumstances including income &amp; asset variations, and provide further advice within the first 12 months of initial advice statement.</p></div></div>
    <div class="option" style="top:160px"><span class="box"></span><div><h3>Annual Review $990</h3><p>A review of the recommendations made in our original advice document, taking into account any changes to client's circumstances including checking current cash flow is sufficient to meet ongoing aged care costs.</p></div></div>
    <div class="option" style="top:217px"><span class="box"></span><div><h3>Post Entry Review $660</h3><p>Review financial situation, check facility invoices are accurate, explain the Residential Aged Care Agreement and ensure all recommendations are implemented.</p></div></div>
    <div class="option" style="top:264px"><span class="box"></span><div><h3>Facility Liason $550</h3><p>Negotiate with the Aged Care Facility regarding Accommodation payments, clarify &amp; explain Residential Care Agreement, and review facility invoices.</p></div></div>
    <div class="option" style="top:308px"><span class="box"></span><div><h3>Family Conferences $660</h3><p>Facilitate &amp; co-ordinate family meetings to explain the Aged Care legislation and how it fits with the family circumstances.</p></div></div>
    <div class="option" style="top:354px"><span class="box"></span><div><h3>Estate Wrap $660</h3><p>Assist beneficiaries with correct procedures and paperwork regarding the finalisation of the estate.</p></div></div>

    <div class="sign-off">
      <p>I/We have chosen the Service Package and Options as ticked above.  I/We understand that by choosing the Essentials Package, that I/We are receiving factual information only, and not financial advice.  I/We agree to pay the amount of ________________________ , within seven days of the date of the invoice received from Silver Harbour SA.</p>
      <div class="dateline" style="left:410px;top:96px">//</div>
      <div class="sign-row" style="left:12px;top:114px">
        <div class="sign">Signature</div><div class="sign">Signature</div><div class="sign">Signature</div><div class="sign">Date</div>
      </div>
      <div class="dateline" style="left:170px;top:170px">//</div>
      <div class="sign-row" style="left:12px;top:186px">
        <div class="sign">Adviser Signature</div><div class="sign" style="margin-top:-2px">Date</div>
      </div>
    </div>

    <div class="legal">
      <h4>Important Information</h4>
      <p>This document has been prepared by Silver Harbour SA Pty Ltd ABN 12 345 678 901, an Authorised Representative of Keystone Advice Limited ABN 98 765 432 109 AFSL 456789, a wholly owned, non-guaranteed subsidiary of the Southern Cross Banking Group ABN 55 444 333 222.</p>
      <p>Information in this document is based on current regulatory requirements and laws, as at 20 September, 2016 which may be subject to change.  It contains general advice.  It does not take into account your individual objectives, financial situation or needs.  You should consider talking to a financial adviser before making a financial decision.</p>
    </div>
  </div>
</section>

</body>
</html>
```